Create an Engaging Yet Simple Cycle Infographic to be featured in new book

I require a clearly designed, simple to navigate infographic. It will depict a "CYCLE-style" Framework that includes 7-stages which are underpinned by 6-enablers. The cycle is the core concept of a new business book. Each component also needs a simple graphic/ icon that can be used as a short-cut to identify the specific stage or enabler. The attached brief provides further details.

Target Market(s)

Business leaders

Font styles to use
Serif

Colors
000000

Requirements
Must have
• Simple, easy to engage with, fit on portrait-oriented book page

```html
<!DOCTYPE html>
<html lang="en">
<head>
<meta charset="utf-8">
<title>Cycle Framework: Seven Stages and Six Enablers</title>
<link rel="stylesheet" href="https://fonts.googleapis.com/css2?family=Open+Sans:wght@700;800&display=swap">
<style>
  :root {
    --page: #f1f1f1;
    --wheel-dark: #3c3949;
    --ring-orange: #f6a71e;
    --ring-text: #2f2c3a;
    --stem-grey: #d9d9d9;
    --ground-brown: #c59b6b;
    --line-white: #ffffff;
    --icon-tone: #3c3949;
  }
  html, body {
    margin: 0;
    padding: 0;
    overflow: hidden;
    background: var(--page);
  }
  .canvas {
    position: relative;
    width: 783px;
    height: 1200px;
    overflow: hidden;
    background: var(--page);
  }
  .framework {
    position: absolute;
    inset: 0;
    width: 783px;
    height: 1200px;
  }
  .stage-label {
    font-family: "Open Sans", Arial, sans-serif;
    font-weight: 800;
    font-size: 37px;
    letter-spacing: 3px;
    fill: var(--ring-text);
  }
  .enabler-label {
    font-family: "Open Sans", Arial, sans-serif;
    font-weight: 700;
    font-size: 17px;
    fill: var(--line-white);
    text-anchor: middle;
  }
</style>
</head>
<body>
<main class="canvas">
  <svg class="framework" viewBox="0 0 783 1200" xmlns="http://www.w3.org/2000/svg">
    <defs>
      <path id="ring-path" d="M 391 688 A 297 297 0 1 1 391.01 688"/>
    </defs>

    <!-- stem -->
    <rect class="stem" x="371" y="600" width="40" height="260" fill="var(--stem-grey)"/>

    <!-- ground -->
    <path class="ground" d="M 0 905 Q 391 805 783 905 L 783 1200 L 0 1200 Z" fill="var(--ground-brown)"/>

    <!-- outer stage ring -->
    <circle class="stage-ring" cx="391" cy="391" r="297" fill="none" stroke="var(--ring-orange)" stroke-width="74"/>
    <g class="ring-gaps" stroke="var(--page)" stroke-width="5">
      <line x1="391" y1="391" x2="391" y2="54" transform="rotate(-6 391 391)"/>
      <line x1="391" y1="391" x2="391" y2="54" transform="rotate(33 391 391)"/>
      <line x1="391" y1="391" x2="391" y2="54" transform="rotate(103 391 391)"/>
      <line x1="391" y1="391" x2="391" y2="54" transform="rotate(172 391 391)"/>
      <line x1="391" y1="391" x2="391" y2="54" transform="rotate(243 391 391)"/>
      <line x1="391" y1="391" x2="391" y2="54" transform="rotate(282 391 391)"/>
      <line x1="391" y1="391" x2="391" y2="54" transform="rotate(318 391 391)"/>
    </g>
    <circle cx="391" cy="391" r="258" fill="var(--page)"/>

    <g class="stage-labels" text-anchor="middle" dominant-baseline="central">
      <text class="stage-label"><textPath href="#ring-path" startOffset="50.6%">SEE</textPath></text>
      <text class="stage-label"><textPath href="#ring-path" startOffset="68.9%">UNDERSTAND</textPath></text>
      <text class="stage-label"><textPath href="#ring-path" startOffset="88.2%">PRIORITISE</textPath></text>
      <text class="stage-label"><textPath href="#ring-path" startOffset="7.4%">DESIGN</textPath></text>
      <text class="stage-label"><textPath href="#ring-path" startOffset="22.5%">PLAN</textPath></text>
      <text class="stage-label"><textPath href="#ring-path" startOffset="33.3%">MOVE</textPath></text>
      <text class="stage-label"><textPath href="#ring-path" startOffset="43.3%">LEARN</textPath></text>
    </g>

    <!-- stage wheel -->
    <circle class="stage-wheel" cx="391" cy="391" r="232" fill="var(--wheel-dark)"/>
    <g class="wheel-dividers" stroke="var(--line-white)" stroke-width="4">
      <line x1="391" y1="391" x2="391" y2="159" transform="rotate(-6 391 391)"/>
      <line x1="391" y1="391" x2="391" y2="159" transform="rotate(33 391 391)"/>
      <line x1="391" y1="391" x2="391" y2="159" transform="rotate(103 391 391)"/>
      <line x1="391" y1="391" x2="391" y2="159" transform="rotate(172 391 391)"/>
      <line x1="391" y1="391" x2="391" y2="159" transform="rotate(243 391 391)"/>
      <line x1="391" y1="391" x2="391" y2="159" transform="rotate(282 391 391)"/>
      <line x1="391" y1="391" x2="391" y2="159" transform="rotate(318 391 391)"/>
    </g>

    <!-- stage icons -->
    <g class="stage-icons" fill="var(--line-white)">
      <g class="icon-see" transform="translate(420 240)">
        <path d="M -30 0 Q 0 -24 30 0 Q 0 24 -30 0 Z"/>
        <circle r="10" fill="var(--wheel-dark)"/>
        <circle r="4"/>
      </g>
      <ellipse class="icon-understand" cx="510" cy="320" rx="28" ry="22" role="img" aria-label="Understand stage icon: thinking head"/>
      <path class="icon-prioritise" transform="translate(510 455)" d="M 0 -30 L 8 -9 L 30 -9 L 12 5 L 19 27 L 0 14 L -19 27 L -12 5 L -30 -9 L -8 -9 Z"/>
      <g class="icon-design" transform="translate(350 535)">
        <rect x="-24" y="-28" width="48" height="56" rx="4"/>
        <g stroke="var(--wheel-dark)" stroke-width="4">
          <line x1="-14" y1="-12" x2="14" y2="-12"/>
          <line x1="-14" y1="0" x2="14" y2="0"/>
          <line x1="-14" y1="12" x2="8" y2="12"/>
        </g>
      </g>
      <g class="icon-plan" transform="translate(280 432)">
        <rect x="-32" y="-16" width="64" height="32" rx="3"/>
        <line x1="0" y1="-16" x2="0" y2="16" stroke="var(--wheel-dark)" stroke-width="3"/>
      </g>
      <g class="icon-move" transform="translate(278 350)" role="img" aria-label="Move stage icon: connected nodes">
        <circle cx="-16" cy="-10" r="10"/>
        <circle cx="14" cy="10" r="10"/>
        <line x1="-16" y1="-10" x2="14" y2="10" stroke="var(--line-white)" stroke-width="4"/>
      </g>
      <g class="icon-learn" transform="translate(328 262)" role="img" aria-label="Learn stage icon: speech bubbles">
        <rect x="-22" y="-20" width="30" height="24" rx="5"/>
        <rect x="0" y="0" width="26" height="22" rx="5"/>
      </g>
    </g>

    <!-- enabler connectors -->
    <g class="enabler-links" stroke="var(--line-white)" stroke-width="4" fill="none">
      <line x1="391" y1="862" x2="391" y2="908"/>
      <line x1="91" y1="908" x2="692" y2="908"/>
      <line x1="91" y1="908" x2="91" y2="960"/>
      <line x1="211" y1="908" x2="211" y2="960"/>
      <line x1="331" y1="908" x2="331" y2="960"/>
      <line x1="452" y1="908" x2="452" y2="960"/>
      <line x1="572" y1="908" x2="572" y2="960"/>
      <line x1="692" y1="908" x2="692" y2="960"/>
    </g>

    <!-- enablers -->
    <g class="enablers">
      <g class="enabler" transform="translate(91 1003)">
        <circle r="42" fill="var(--line-white)"/>
        <rect x="-12" y="-26" width="24" height="52" rx="10" fill="var(--icon-tone)" role="img" aria-label="Enduring Commitment icon"/>
      </g>
      <g class="enabler" transform="translate(211 1003)">
        <circle r="42" fill="var(--line-white)"/>
        <path d="M -28 14 A 28 28 0 0 1 28 14 Z" fill="var(--icon-tone)" role="img" aria-label="Adaptive Mindset icon"/>
      </g>
      <g class="enabler" transform="translate(331 1003)" fill="none" stroke="var(--icon-tone)" stroke-width="5" stroke-linecap="round">
        <circle r="42" fill="var(--line-white)" stroke="none"/>
        <circle cx="0" cy="-22" r="6"/>
        <line x1="0" y1="-16" x2="0" y2="26"/>
        <line x1="-12" y1="-6" x2="12" y2="-6"/>
        <path d="M -24 8 Q -20 26 0 26 Q 20 26 24 8"/>
      </g>
      <g class="enabler" transform="translate(452 1003)">
        <circle r="42" fill="var(--line-white)"/>
        <rect x="-9" y="-28" width="18" height="56" rx="9" fill="var(--icon-tone)" role="img" aria-label="The Golden Thread icon"/>
      </g>
      <g class="enabler" transform="translate(572 1003)">
        <circle r="42" fill="var(--line-white)"/>
        <path d="M -26 20 L 0 -28 L 26 20 Z" fill="var(--icon-tone)" role="img" aria-label="Adaptive Leadership icon"/>
      </g>
      <g class="enabler" transform="translate(692 1003)" stroke="var(--icon-tone)" stroke-width="4" fill="none" stroke-linecap="round">
        <circle r="42" fill="var(--line-white)" stroke="none"/>
        <line x1="0" y1="-26" x2="0" y2="24"/>
        <line x1="-24" y1="-16" x2="24" y2="-16"/>
        <line x1="-14" y1="24" x2="14" y2="24"/>
        <path d="M -32 4 L -24 -16 L -16 4 Z M 16 4 L 24 -16 L 32 4 Z" fill="var(--icon-tone)"/>
      </g>
    </g>

    <g class="enabler-labels">
      <text class="enabler-label" x="91" y="1082">Enduring</text>
      <text class="enabler-label" x="91" y="1103">Commitment</text>
      <text class="enabler-label" x="211" y="1082">Adaptive</text>
      <text class="enabler-label" x="211" y="1103">Mindset</text>
      <text class="enabler-label" x="331" y="1082">Anchors</text>
      <text class="enabler-label" x="331" y="1103">of Certainty</text>
      <text class="enabler-label" x="452" y="1082">The Golden</text>
      <text class="enabler-label" x="452" y="1103">Thread</text>
      <text class="enabler-label" x="572" y="1082">Adaptive</text>
      <text class="enabler-label" x="572" y="1103">Leadership</text>
      <text class="enabler-label" x="692" y="1082">Balanced</text>
      <text class="enabler-label" x="692" y="1103">Ecosystem</text>
    </g>
  </svg>
</main>
</body>
</html>
```